Unique Playing Card Deck Design

Brief:

I am looking for a designer to design a whole deck of cards from the ground up. I would like both the front and back designed for the deck, and would like the desk to include all the standard cards including jokers. I would like to make each card as unique as possible, so including original designs and artwork for the non-face cards as well.

I would like these cards to be poker size (63mm x 88mm, 2.5" x 3.5") or B8 size according to ISO 216) and I’ve attached a template that should be followed for the sizing.

No real limit on the design so be as creative as you can!

Design Details

Color Mode: RGB or CYMK for color images, Grayscale for black and white

File types: JPG, BMP, PNG, GIF, TIFF

Image resolution: Minimum 300 dpi

Bleeding: Allow 1/8" (approx 36 pixels based on a 300dpi image) for bleeding and a further 1/8" for safe area margin inside each side

EDIT: Because this project requires a lot of design work I am fine for the submissions to be limited to 3 or 4 cards that would demonstrate the overall direction that you are taking. Once I have chosen the designs we can continue refining them and adding the rest of the deck. I would also like a box for the cards to be designed and can provide a template after I have chosen the designers. Thanks and please let me know if you have any questions!

EDIT2: I realize this project is a lot of work and so I have taken the amounts that I had for 2nd and 3rd place and increased the reward for 1st place. I am still interested in selecting multiple designs, but because this project is being done on a committed payment basis I wanted to ensure that I was only obligated to select one design. However, if there are multiple designs that I am interested in, I will award the design work to an additional 1-3 designers (to a maximum of 4 total) on the same terms as 1st place. i.e. all designers selected will be paid the same amount. Thanks again for looking!

Target Market(s)

Adult card players who appreciate good design (i.e. the designs should not be cartoon-like or targeted at children). These are going to be premium cards printed on the best quality paper etc so I would like the design to reflect this.

Font styles to use
Decorative
Script

Requirements
Nice to have
• I will leave the design idea up to you but I like the look of really old playing cards (think of a deck of medieval playing cards for example). I also like the art deco kind of aesthetic. On the complete opposite side of the spectrum a very modern looking, minimalist design is also appealing.
• These are just a few ideas but as I said I am really open to anything. It just needs to be a bold, original design.

```html
<!DOCTYPE html>
<html lang="en">
<head>
<meta charset="utf-8">
<title>Playing Card Deck</title>
<link rel="stylesheet" href="https://fonts.googleapis.com/css2?family=Playfair+Display:ital,wght@0,700;0,900;1,700&display=swap">
<style>
:root{
  --page:#ffffff;
  --card:#e23b82;
  --card-edge:#a81f5a;
  --band:#c42a6b;
  --frame:#f0679f;
  --pip:#8c1745;
  --gold:#f6d21f;
  --back-dark:#3a0a22;
  --back-mid:#7a1646;
  --joker-a:#f07aa6;
  --joker-b:#c8b45a;
}
*{margin:0;padding:0;box-sizing:border-box}
html,body{width:1200px;height:463px;overflow:hidden;background:var(--page)}
.deck{
  position:absolute;left:3px;top:3px;
  display:grid;
  grid-template-columns:repeat(14,80px);
  grid-template-rows:repeat(4,108px);
  column-gap:5.9px;row-gap:8px;
}
.card{
  position:relative;width:80px;height:108px;
  background:
    linear-gradient(135deg,transparent 15%,var(--band) 15% 23%,transparent 23% 77%,var(--band) 77% 85%,transparent 85%),
    var(--card);
  border:3px solid var(--card-edge);
  box-shadow:inset 0 0 0 4px var(--card),inset 0 0 0 5px var(--frame);
  font-family:"Playfair Display",serif;font-weight:900;color:var(--gold);
  font-variant-numeric:lining-nums;
  overflow:hidden;
}
.rank{position:absolute;font-size:9px;line-height:1}
.rank.top{left:4px;top:3px}
.rank.bottom{right:4px;bottom:3px;transform:rotate(180deg)}
.pip{position:absolute;left:50%;top:50%;width:34px;height:42px;transform:translate(-50%,-50%);fill:var(--pip)}
.pip-rank{position:absolute;left:0;right:0;top:50%;transform:translateY(-50%);text-align:center;font-size:10px;line-height:1}
.face .pip-rank{font-size:12px}
.joker-mark{position:absolute;font-size:5px;letter-spacing:.3px;line-height:1}
.joker-mark.top{left:4px;top:5px}
.joker-mark.bottom{right:4px;bottom:5px;transform:rotate(180deg)}
.joker-art{position:absolute;left:50%;top:50%;width:30px;height:46px;transform:translate(-50%,-50%);border-radius:8px;background:linear-gradient(180deg,var(--joker-a),var(--joker-b))}
.card-back{
  position:relative;width:80px;height:108px;
  background:linear-gradient(135deg,var(--back-dark),var(--back-mid) 55%,var(--back-dark));
  border:2px solid var(--card-edge);
  overflow:hidden;
}
.back-pattern{position:absolute;inset:0;background:linear-gradient(160deg,rgba(255,255,255,.06),rgba(0,0,0,.15))}
.back-name{position:absolute;left:0;right:0;top:45px;text-align:center;font-family:"Playfair Display",serif;font-weight:900;color:var(--gold);font-size:13px;line-height:1}
.back-label{position:absolute;left:0;right:0;top:36px;text-align:center;font-family:"Playfair Display",serif;font-weight:700;font-style:italic;color:var(--gold);font-size:13px;line-height:1.3}
</style>
</head>
<body>
<svg width="0" height="0" style="position:absolute" aria-hidden="true">
  <defs>
    <symbol id="suit-diamond" viewBox="0 0 40 50"><path d="M20 2 L38 25 L20 48 L2 25Z"/></symbol>
    <symbol id="suit-heart" viewBox="0 0 40 50"><path d="M20 46C8 34 2 27 2 17 2 9 8 4 14 4c3 0 5 2 6 5 1-3 3-5 6-5 6 0 12 5 12 13 0 10-6 17-18 29Z"/></symbol>
    <symbol id="suit-spade" viewBox="0 0 40 50"><path d="M20 3C8 16 2 22 2 31c0 7 5 11 10 11 3 0 6-2 7-4l-3 10h8l-3-10c1 2 4 4 7 4 5 0 10-4 10-11 0-9-6-15-18-28Z"/></symbol>
    <symbol id="suit-club" viewBox="0 0 40 50"><circle cx="20" cy="13" r="10"/><circle cx="10" cy="28" r="10"/><circle cx="30" cy="28" r="10"/><path d="M18 26h4l3 22h-10Z"/></symbol>
  </defs>
</svg>

<main class="deck">
  <!-- Diamonds -->
  <div class="card"><span class="rank top">A</span><svg class="pip"><use href="#suit-diamond"/></svg><span class="pip-rank">A</span><span class="rank bottom">A</span></div>
  <div class="card"><span class="rank top">2</span><svg class="pip"><use href="#suit-diamond"/></svg><span class="pip-rank">2</span><span class="rank bottom">2</span></div>
  <div class="card"><span class="rank top">3</span><svg class="pip"><use href="#suit-diamond"/></svg><span class="pip-rank">3</span><span class="rank bottom">3</span></div>
  <div class="card"><span class="rank top">4</span><svg class="pip"><use href="#suit-diamond"/></svg><span class="pip-rank">4</span><span class="rank bottom">4</span></div>
  <div class="card"><span class="rank top">5</span><svg class="pip"><use href="#suit-diamond"/></svg><span class="pip-rank">5</span><span class="rank bottom">5</span></div>
  <div class="card"><span class="rank top">6</span><svg class="pip"><use href="#suit-diamond"/></svg><span class="pip-rank">6</span><span class="rank bottom">6</span></div>
  <div class="card"><span class="rank top">7</span><svg class="pip"><use href="#suit-diamond"/></svg><span class="pip-rank">7</span><span class="rank bottom">7</span></div>
  <div class="card"><span class="rank top">8</span><svg class="pip"><use href="#suit-diamond"/></svg><span class="pip-rank">8</span><span class="rank bottom">8</span></div>
  <div class="card"><span class="rank top">9</span><svg class="pip"><use href="#suit-diamond"/></svg><span class="pip-rank">9</span><span class="rank bottom">9</span></div>
  <div class="card"><span class="rank top">10</span><svg class="pip"><use href="#suit-diamond"/></svg><span class="pip-rank">10</span><span class="rank bottom">10</span></div>
  <div class="card face"><span class="rank top">K</span><svg class="pip"><use href="#suit-diamond"/></svg><span class="pip-rank">K</span><span class="rank bottom">K</span></div>
  <div class="card face"><span class="rank top">Q</span><svg class="pip"><use href="#suit-diamond"/></svg><span class="pip-rank">Q</span><span class="rank bottom">Q</span></div>
  <div class="card face"><span class="rank top">J</span><svg class="pip"><use href="#suit-diamond"/></svg><span class="pip-rank">J</span><span class="rank bottom">J</span></div>
  <div class="card joker"><span class="joker-mark top">JOKER</span><div class="joker-art" role="img" aria-label="Joker character illustration"></div><span class="joker-mark bottom">JOKER</span></div>

  <!-- Hearts -->
  <div class="card"><span class="rank top">A</span><svg class="pip"><use href="#suit-heart"/></svg><span class="pip-rank">A</span><span class="rank bottom">A</span></div>
  <div class="card"><span class="rank top">2</span><svg class="pip"><use href="#suit-heart"/></svg><span class="pip-rank">2</span><span class="rank bottom">2</span></div>
  <div class="card"><span class="rank top">3</span><svg class="pip"><use href="#suit-heart"/></svg><span class="pip-rank">3</span><span class="rank bottom">3</span></div>
  <div class="card"><span class="rank top">4</span><svg class="pip"><use href="#suit-heart"/></svg><span class="pip-rank">4</span><span class="rank bottom">4</span></div>
  <div class="card"><span class="rank top">5</span><svg class="pip"><use href="#suit-heart"/></svg><span class="pip-rank">5</span><span class="rank bottom">5</span></div>
  <div class="card"><span class="rank top">6</span><svg class="pip"><use href="#suit-heart"/></svg><span class="pip-rank">6</span><span class="rank bottom">6</span></div>
  <div class="card"><span class="rank top">7</span><svg class="pip"><use href="#suit-heart"/></svg><span class="pip-rank">7</span><span class="rank bottom">7</span></div>
  <div class="card"><span class="rank top">8</span><svg class="pip"><use href="#suit-heart"/></svg><span class="pip-rank">8</span><span class="rank bottom">8</span></div>
  <div class="card"><span class="rank top">9</span><svg class="pip"><use href="#suit-heart"/></svg><span class="pip-rank">9</span><span class="rank bottom">9</span></div>
  <div class="card"><span class="rank top">10</span><svg class="pip"><use href="#suit-heart"/></svg><span class="pip-rank">10</span><span class="rank bottom">10</span></div>
  <div class="card face"><span class="rank top">K</span><svg class="pip"><use href="#suit-heart"/></svg><span class="pip-rank">K</span><span class="rank bottom">K</span></div>
  <div class="card face"><span class="rank top">Q</span><svg class="pip"><use href="#suit-heart"/></svg><span class="pip-rank">Q</span><span class="rank bottom">Q</span></div>
  <div class="card face"><span class="rank top">J</span><svg class="pip"><use href="#suit-heart"/></svg><span class="pip-rank">J</span><span class="rank bottom">J</span></div>
  <div class="card joker"><span class="joker-mark top">JOKER</span><div class="joker-art" role="img" aria-label="Second joker character illustration"></div><span class="joker-mark bottom">JOKER</span></div>

  <!-- Spades -->
  <div class="card"><span class="rank top">A</span><svg class="pip"><use href="#suit-spade"/></svg><span class="pip-rank">A</span><span class="rank bottom">A</span></div>
  <div class="card"><span class="rank top">2</span><svg class="pip"><use href="#suit-spade"/></svg><span class="pip-rank">2</span><span class="rank bottom">2</span></div>
  <div class="card"><span class="rank top">3</span><svg class="pip"><use href="#suit-spade"/></svg><span class="pip-rank">3</span><span class="rank bottom">3</span></div>
  <div class="card"><span class="rank top">4</span><svg class="pip"><use href="#suit-spade"/></svg><span class="pip-rank">4</span><span class="rank bottom">4</span></div>
  <div class="card"><span class="rank top">5</span><svg class="pip"><use href="#suit-spade"/></svg><span class="pip-rank">5</span><span class="rank bottom">5</span></div>
  <div class="card"><span class="rank top">6</span><svg class="pip"><use href="#suit-spade"/></svg><span class="pip-rank">6</span><span class="rank bottom">6</span></div>
  <div class="card"><span class="rank top">7</span><svg class="pip"><use href="#suit-spade"/></svg><span class="pip-rank">7</span><span class="rank bottom">7</span></div>
  <div class="card"><span class="rank top">8</span><svg class="pip"><use href="#suit-spade"/></svg><span class="pip-rank">8</span><span class="rank bottom">8</span></div>
  <div class="card"><span class="rank top">9</span><svg class="pip"><use href="#suit-spade"/></svg><span class="pip-rank">9</span><span class="rank bottom">9</span></div>
  <div class="card"><span class="rank top">10</span><svg class="pip"><use href="#suit-spade"/></svg><span class="pip-rank">10</span><span class="rank bottom">10</span></div>
  <div class="card face"><span class="rank top">K</span><svg class="pip"><use href="#suit-spade"/></svg><span class="pip-rank">K</span><span class="rank bottom">K</span></div>
  <div class="card face"><span class="rank top">Q</span><svg class="pip"><use href="#suit-spade"/></svg><span class="pip-rank">Q</span><span class="rank bottom">Q</span></div>
  <div class="card face"><span class="rank top">J</span><svg class="pip"><use href="#suit-spade"/></svg><span class="pip-rank">J</span><span class="rank bottom">J</span></div>
  <div class="card-back"><div class="back-pattern" role="img" aria-label="Hexagon pattern on card back"></div><span class="back-name">Vellora</span></div>

  <!-- Clubs -->
  <div class="card"><span class="rank top">A</span><svg class="pip"><use href="#suit-club"/></svg><span class="pip-rank">A</span><span class="rank bottom">A</span></div>
  <div class="card"><span class="rank top">2</span><svg class="pip"><use href="#suit-club"/></svg><span class="pip-rank">2</span><span class="rank bottom">2</span></div>
  <div class="card"><span class="rank top">3</span><svg class="pip"><use href="#suit-club"/></svg><span class="pip-rank">3</span><span class="rank bottom">3</span></div>
  <div class="card"><span class="rank top">4</span><svg class="pip"><use href="#suit-club"/></svg><span class="pip-rank">4</span><span class="rank bottom">4</span></div>
  <div class="card"><span class="rank top">5</span><svg class="pip"><use href="#suit-club"/></svg><span class="pip-rank">5</span><span class="rank bottom">5</span></div>
  <div class="card"><span class="rank top">6</span><svg class="pip"><use href="#suit-club"/></svg><span class="pip-rank">6</span><span class="rank bottom">6</span></div>
  <div class="card"><span class="rank top">7</span><svg class="pip"><use href="#suit-club"/></svg><span class="pip-rank">7</span><span class="rank bottom">7</span></div>
  <div class="card"><span class="rank top">8</span><svg class="pip"><use href="#suit-club"/></svg><span class="pip-rank">8</span><span class="rank bottom">8</span></div>
  <div class="card"><span class="rank top">9</span><svg class="pip"><use href="#suit-club"/></svg><span class="pip-rank">9</span><span class="rank bottom">9</span></div>
  <div class="card"><span class="rank top">10</span><svg class="pip"><use href="#suit-club"/></svg><span class="pip-rank">10</span><span class="rank bottom">10</span></div>
  <div class="card face"><span class="rank top">K</span><svg class="pip"><use href="#suit-club"/></svg><span class="pip-rank">K</span><span class="rank bottom">K</span></div>
  <div class="card face"><span class="rank top">Q</span><svg class="pip"><use href="#suit-club"/></svg><span class="pip-rank">Q</span><span class="rank bottom">Q</span></div>
  <div class="card face"><span class="rank top">J</span><svg class="pip"><use href="#suit-club"/></svg><span class="pip-rank">J</span><span class="rank bottom">J</span></div>
  <div class="card-back"><div class="back-pattern" role="img" aria-label="Hexagon pattern on card back"></div><span class="back-label">card<br>back</span></div>
</main>
</body>
</html>
```